website for 'thebrightnook' which is a specialise tutoring company for children with learning difficu

We need a website for a new business that is focused on assessment and then specialised tutoring for young children with learning difficulties. The website needs to be simple but fun and fresh. We have an existing logo (uploaded) that needs to be the building block for the website. The website doesn't need to be overly content-heavy.

Target Market(s)

parents

Industry/Entity Type

Education

Number of Pages Required

3 page

Font styles to use
Other font styles liked:
• possibly matched to the logo

Requirements
Must have
• a initial front page which introduces the business and provides contact details, a second page that will allow for a more content-heavy section, a third page which focuses on introducing the staff (initially 3 staff ),

```html
<!DOCTYPE html>
<html lang="en">
<head>
<meta charset="utf-8">
<title>thebrightnook – science: exploring volume</title>
<link rel="stylesheet" href="https://fonts.googleapis.com/css2?family=Arimo:wght@400;700&family=Kameron:wght@400;700&family=Montserrat:wght@400&display=swap">
<style>
:root{
  --paper:#f4f0e7;
  --kraft:#c6b194;
  --green:#7cc242;
  --green-dark:#4e8a1c;
  --ink:#2d2b28;
  --body:#3a3836;
  --muted:#8d8a85;
  --menu:#4a4a4a;
  --menu-hi:#343434;
  --footer-ink:#5a5046;
  --white:#ffffff;
}
*{margin:0;padding:0;box-sizing:border-box}
html,body{width:1200px;height:1061px;overflow:hidden}
body{background:var(--paper);font-family:"Arimo",Arial,sans-serif;color:var(--body);position:relative}
.header{position:absolute;left:0;top:0;width:1200px;height:222px;background:var(--white)}
.brand{position:absolute;left:116px;top:40px}
.brand-dot{position:absolute;left:110px;top:0;width:56px;height:56px;border-radius:50%;background:var(--green)}
.brand-name{position:absolute;left:0;top:68px;font-family:"Kameron",Georgia,serif;font-weight:400;font-size:50px;letter-spacing:-1.5px;color:var(--ink);white-space:nowrap;line-height:1}
.brand-tag{position:absolute;left:0;top:135px;font-family:"Kameron",Georgia,serif;font-size:14.5px;letter-spacing:2.6px;color:var(--muted);white-space:nowrap}
.social{position:absolute;top:12px;left:806px;display:flex;align-items:center;gap:10px}
.social .dot{width:28px;height:28px;border-radius:50%;background:var(--green)}
.social .sep{width:1px;height:24px;background:#d8d8d8;margin:0 2px}
.subscribe{font-family:"Kameron",Georgia,serif;font-weight:700;font-style:italic;font-size:17px;color:var(--muted);margin-left:2px}
.nav{position:absolute;left:490px;top:166px;display:flex;align-items:center;font-family:"Kameron",Georgia,serif;font-size:17.5px;color:var(--ink)}
.nav a{color:inherit;text-decoration:none;padding:6px 9px;line-height:21px}
.nav .bar{width:1px;height:20px;background:#cfcfcf;margin:0 6px}
.nav a.active{background:var(--green);border-radius:4px 4px 0 0;padding:6px 8px}
.dropdown{position:absolute;left:876px;top:202px;width:158px;background:var(--menu);border-radius:0 0 4px 4px;box-shadow:0 3px 6px rgba(0,0,0,.35);z-index:3;font-family:"Montserrat",Arial,sans-serif;font-size:12.5px;color:#e8e8e8}
.dropdown li{list-style:none;height:36.5px;line-height:36.5px;padding-left:25px;border-top:1px solid #5a5a5a}
.dropdown li:first-child{border-top:0}
.dropdown li.current{background:var(--menu-hi)}
.band-top{position:absolute;left:0;top:220px;width:1200px;height:62px;background:var(--kraft);box-shadow:0 3px 5px rgba(0,0,0,.12)}
.photo-frame{position:absolute;background:var(--white);box-shadow:0 2px 5px rgba(0,0,0,.18);border:1px solid #e2e2e2}
.main-photo{left:116px;top:320px;width:368px;height:526px}
.main-photo .fill{position:absolute;left:9px;top:9px;width:347px;height:502px;background:linear-gradient(160deg,#cfc9c0 0%,#b9a78c 35%,#e4dfb9 60%,#8a7a66 100%)}
.thumb-photo{left:116px;top:866px;width:366px;height:125px}
.thumb-photo .fill{position:absolute;left:9px;top:9px;width:346px;height:105px;background:linear-gradient(90deg,#9fb8c6 0%,#6fa9cc 40%,#dfe6ea 75%,#8fb6cf 100%)}
.lesson-title{position:absolute;left:484px;top:320px;width:388px;height:41px;background:var(--green);font-family:"Kameron",Georgia,serif;font-weight:400;font-size:27px;color:var(--ink);line-height:41px;padding-left:30px;white-space:nowrap}
.lesson{position:absolute;left:514px;top:384px;width:580px}
.lesson h3{font-size:16.5px;font-weight:700;color:#444;margin-bottom:12px}
.supplies{list-style:none;margin-left:15px;font-size:15px;line-height:20.2px;color:#555}
.lesson p{font-size:16px;line-height:25.9px;color:#222;margin-top:24px;letter-spacing:-0.1px}
.lesson p+p{margin-top:26px}
.lesson-links{position:absolute;left:514px;top:919px;font-size:13.4px;color:var(--green-dark);display:flex;gap:12px}
.lesson-links .pipe{color:#bbb}
.filed{position:absolute;left:516px;top:969px;font-family:"Kameron",Georgia,serif;font-size:13.4px;color:var(--muted);display:flex;align-items:center;gap:6px}
.footer{position:absolute;left:0;top:1003px;width:1200px;height:58px;background:var(--kraft)}
.footer-social{position:absolute;left:118px;top:1019px;display:flex;gap:12px}
.footer-social .dot{width:27px;height:27px;border-radius:50%;background:#8f8373}
.footer-name{position:absolute;right:121px;top:1011px;font-family:"Kameron",Georgia,serif;font-size:20px;letter-spacing:-.5px;color:var(--footer-ink)}
.copyright{position:absolute;right:120px;top:1039px;font-size:12px;color:var(--footer-ink)}
</style>
</head>
<body>
<header class="header">
  <div class="brand">
    <span class="brand-dot"></span>
    <div class="brand-name">thebrightnook</div>
    <div class="brand-tag">specialised learning for children</div>
  </div>
  <div class="social">
    <span class="dot"></span><span class="dot"></span><span class="dot"></span>
    <span class="sep"></span>
    <svg width="28" height="26" viewBox="0 0 28 26" aria-label="basket"><path d="M3 10h22l-3 13H6z" fill="var(--green)"/><path d="M9 10l5-7 5 7" stroke="var(--green)" stroke-width="2.5" fill="none"/></svg>
    <span class="sep"></span>
    <span class="subscribe">Subscribe</span>
    <svg width="26" height="20" viewBox="0 0 26 20" aria-label="email"><rect x="1" y="2" width="24" height="16" fill="var(--green)"/><path d="M1 2l12 10 12-10" stroke="#fff" stroke-width="2" fill="none"/></svg>
  </div>
  <nav class="nav">
    <a href="#">home</a><span class="bar"></span>
    <a href="#">about us</a><span class="bar"></span>
    <a href="#">tutoring</a><span class="bar"></span>
    <a href="#">assessments</a><span class="bar"></span>
    <a href="#" class="active">lesson plans</a><span class="bar"></span>
    <a href="#">contact us</a>
  </nav>
</header>

<div class="band-top" aria-hidden="true"></div>

<ul class="dropdown">
  <li>Arts &amp; Crafts</li>
  <li class="current">Mathematics</li>
  <li>Movement</li>
  <li>Music &amp; Rhythm</li>
  <li>Science</li>
</ul>

<div class="photo-frame main-photo"><div class="fill" role="img" aria-label="Photo of a young girl pouring blue water between glass science flasks at a table"></div></div>
<div class="photo-frame thumb-photo"><div class="fill" role="img" aria-label="Photo of clear bottles and containers filled with blue water"></div></div>

<h2 class="lesson-title">science: exploring volume</h2>

<section class="lesson">
  <h3>Supplies you will need:</h3>
  <ul class="supplies">
    <li>* Plastic 1 or 2 Cup Measuring Container</li>
    <li>* Plastic Pitcher of Water</li>
    <li>* Funnel</li>
    <li>* Food Coloring</li>
    <li>* Variety of Containers in Different Sizes and Shapes</li>
    <li>* Tray and Paper Towels (To Catch Spills)</li>
  </ul>
  <p>Fill a plastic measuring jug with enough water the kids can manage pouring. We refilled our pitcher once. Add food coloring as desired. Adding a bit of color is fun for kids, and it helps them to see the volume of water in each container better. Place a variety of containers on a tray or table. I also set out a funnel to use with the water bottles. Water bottles, food storage containers, party cups, or any sort of clear container works great for this activity.</p>
  <p>Simple activities like this volume activity are a wonderful way to get kids thinking, exploring, problem solving, and observing what is happening around them. You can try this activity with a number of materials including small blocks, shells, gems, sand, and rocks. Setting up two stations, one for liquids and one for solids, is a great way for kids to explore volume with a variety of materials.</p>
</section>

<div class="lesson-links">
  <span>Go back to Science Lesson Plans</span><span class="pipe">|</span>
  <span>Download Lesson Plan</span><span class="pipe">|</span>
  <span>See Next Lesson Plan</span>
</div>

<div class="filed">
  <svg width="16" height="13" viewBox="0 0 16 13" aria-hidden="true"><path d="M0 1h6l2 2h7v10H0z" fill="#a9a59f"/></svg>
  <span>Filed Under: Lesson Plans, Science</span>
  <svg width="14" height="14" viewBox="0 0 14 14" aria-hidden="true"><path d="M0 0h7l7 7-7 7-7-7z" fill="#a9a59f"/><circle cx="3.5" cy="3.5" r="1.3" fill="var(--paper)"/></svg>
  <span>Tagged With: measurement, science</span>
</div>

<footer class="footer" aria-hidden="true"></footer>
<div class="footer-social"><span class="dot"></span><span class="dot"></span><span class="dot"></span></div>
<div class="footer-name">thebrightnook</div>
<div class="copyright">Copyright © thebrightnook 2016</div>
</body>
</html>
```